App Screenshots

We need professional looking screenshots for out apps Thought Arena and Thought Arena Plus.
The screenshots should incorporate text highlighting features or other significant details.
You can see the current screenshots here:
https://apps.example-store.test/details?id=cerebrix.thoughtarena
And here is some of our competition.
Neuro Duels:
https://apps.example-store.test/details?id=kr.co.velquora.neuroduels
Cognivane
https://apps.example-store.test/details?id=com.ferrinworks.cognivane
Some example to use in the screenshots:
Thought Arena "exercise your brain"
Used by over 8 million people
Nearly three dozen brain training games to challenge you daily
Discover your strengths and weaknesses
Exercise a broad range of cognitive skills
Based on principles of cognitive psychology
For the pro version, text can also be added:
The training center selects games for you based on your strengths and weaknesses
The text doesn't have to be exactly the same if you can think of something better, or need to modify it to fit.
We need the ability to modify the text and insert different screenshots into the images. This will allow us to modify them for multiple languages. PSD files preferred. Raw screenshots are attached for convenience.

```html
<!DOCTYPE html>
<html lang="en">
<head>
<meta charset="utf-8">
<title>Thought Arena – Exercise your memory</title>
<link rel="stylesheet" href="https://fonts.googleapis.com/css2?family=Hind:wght@500;600&family=Roboto:wght@400;500;700&family=Noto+Sans+Devanagari&family=Noto+Sans+Tamil&family=Noto+Sans+Ethiopic&family=Noto+Sans+Gurmukhi&display=swap">
<style>
:root{
  --ink:#ffffff;
  --banner:#1b5aa3;
  --device:#1e1e1e;
  --device-edge:#3a3a3a;
  --blue:#2196f3;
  --cyan:#22c3e2;
  --cyan-cell:#29c7e8;
  --orange:#f7870f;
  --peach:#f4c28c;
  --purple:#7a2784;
  --purple-deep:#6a1f74;
  --screen:#ffffff;
}
*{margin:0;padding:0;box-sizing:border-box}
html,body{width:1200px;height:750px;overflow:hidden;background:#fff}
.canvas{position:relative;width:1200px;height:750px;overflow:hidden;font-family:"Roboto",sans-serif}
.scene-photo{position:absolute;inset:0;
  background:
    linear-gradient(90deg,#ffffff 0%,rgba(255,255,255,.85) 6%,rgba(255,255,255,0) 22%),
    linear-gradient(180deg,#7c9a62 0%,#9fb07a 22%,#b9a48e 30%,#8fb367 45%,#a5c77c 65%,#c2d8a0 100%);}
.scene-photo::after{content:"";position:absolute;right:0;top:0;width:360px;height:140px;
  background:radial-gradient(ellipse at 50% 60%,#e0a48e 0%,rgba(224,164,142,0) 70%)}
.headline{position:absolute;left:606px;top:139px;width:594px;height:209px;background:var(--banner);
  border-radius:4px 0 0 4px;box-shadow:0 2px 8px rgba(0,0,0,.25);
  display:flex;align-items:center;justify-content:center;text-align:center;
  color:var(--ink);font-family:"Hind",sans-serif;font-weight:500;font-size:41px;line-height:48px;letter-spacing:.3px}
.phone{position:absolute;top:431px;width:238px;height:340px;background:var(--device);
  border-radius:26px 26px 0 0;border:2px solid var(--device-edge)}
.phone .camera{position:absolute;top:18px;left:50%;width:10px;height:10px;margin-left:-5px;border-radius:50%;background:#444}
.phone .sensor{position:absolute;top:22px;left:35px;width:5px;height:5px;border-radius:50%;background:#333}
.screen{position:absolute;top:36px;left:8px;right:8px;bottom:0;background:var(--screen);overflow:hidden}
.status{height:37px;display:flex;align-items:center;color:#fff;font-size:25px;font-weight:500;padding:0 6px}
.status svg{flex:none}
.status .count{margin-left:8px}
.status .spacer{flex:1}
.p1{left:67px}.p1 .status{background:var(--blue)}
.p2{left:337px}.p2 .status{background:var(--cyan)}
.p3{left:611px}.p3 .status{background:var(--orange)}
.p4{left:881px}.p4 .status{background:var(--purple)}
.arrow{position:absolute;width:23px;height:16px}
.prompt{text-align:center;font-size:17px;font-weight:500;height:26px;line-height:26px}
.p2 .prompt{color:var(--cyan)}
.p3 .prompt{color:var(--orange);font-weight:400}
.p4 .prompt{color:#4a2a50;font-weight:400;text-align:left;padding-left:6px;font-size:16.5px}
.word-list{display:grid;grid-template-columns:1fr 1fr;gap:3px;background:#fff}
.word-list span{background:var(--cyan-cell);height:53px;display:flex;align-items:center;justify-content:center;
  color:#fff;font-weight:500;font-size:21px;white-space:nowrap;overflow:hidden}
.pattern{display:grid;grid-template-columns:repeat(5,37px);gap:3px;margin:9px 0 0 10px}
.pattern i{height:36px;background:var(--peach)}
.pattern i.on{background:var(--orange)}
.symbols{margin:6px 0 0 5px;width:212px;border:4px solid var(--purple-deep);background:var(--purple-deep);
  display:grid;grid-template-columns:repeat(6,1fr);gap:2px}
.symbols span{background:#fff;height:32px;display:flex;align-items:center;justify-content:center;
  color:var(--purple-deep);font-size:17px;
  font-family:"Noto Sans Devanagari","Noto Sans Tamil","Noto Sans Ethiopic","Noto Sans Gurmukhi",sans-serif}
</style>
</head>
<body>
<div class="canvas">
  <div class="scene-photo" role="img" aria-label="Outdoor campus lawn photo of a smiling student with a striped scarf using a smartphone"></div>

  <div class="headline">Exercise your memory,<br>speed, concentration,<br>and more.</div>

  <svg width="0" height="0" style="position:absolute">
    <defs>
      <symbol id="ico-back" viewBox="0 0 14 24"><path d="M12 2 3 12l9 10" fill="none" stroke="#fff" stroke-width="2.2"/></symbol>
      <symbol id="ico-clock" viewBox="0 0 30 30"><circle cx="15" cy="15" r="13" fill="none" stroke="#fff" stroke-width="2"/><path d="M15 6v9l-5 4" fill="none" stroke="#fff" stroke-width="2"/></symbol>
      <symbol id="ico-bolt" viewBox="0 0 30 30"><path d="M24 2 9 16h7L4 28l20-16h-8z" fill="none" stroke="#fff" stroke-width="1.8"/></symbol>
      <symbol id="ico-heart" viewBox="0 0 32 28"><path d="M16 26S2 17 2 9a7 7 0 0 1 14-2 7 7 0 0 1 14 2c0 8-14 17-14 17z" fill="none" stroke="#fff" stroke-width="2"/></symbol>
      <symbol id="ico-arrow" viewBox="0 0 28 20"><path d="M2 7h14V2l10 8-10 8v-5H2z" fill="none" stroke="#2196f3" stroke-width="2.2" stroke-linejoin="round"/></symbol>
    </defs>
  </svg>

  <div class="phone p1"><span class="sensor"></span><span class="camera"></span>
    <div class="screen">
      <div class="status">
        <svg width="13" height="22"><use href="#ico-back"/></svg>
        <svg width="30" height="30" style="margin-left:10px"><use href="#ico-clock"/></svg>
        <span class="count">1</span><span class="spacer"></span>
        <svg width="32" height="28"><use href="#ico-heart"/></svg>
        <span class="count">1</span>
      </div>
      <svg class="arrow" style="left:178px;top:87px"><use href="#ico-arrow"/></svg>
      <svg class="arrow" style="left:139px;top:127px"><use href="#ico-arrow"/></svg>
      <svg class="arrow" style="left:99px;top:166px"><use href="#ico-arrow"/></svg>
      <svg class="arrow" style="left:139px;top:206px"><use href="#ico-arrow"/></svg>
      <svg class="arrow" style="left:178px;top:245px"><use href="#ico-arrow"/></svg>
    </div>
  </div>

  <div class="phone p2"><span class="sensor"></span><span class="camera"></span>
    <div class="screen">
      <div class="status">
        <svg width="13" height="22"><use href="#ico-back"/></svg>
        <svg width="30" height="30" style="margin-left:10px"><use href="#ico-clock"/></svg>
        <span class="count">14</span><span class="spacer"></span>
        <svg width="32" height="28"><use href="#ico-heart"/></svg>
        <span class="count">0</span>
      </div>
      <p class="prompt">Memorize this list</p>
      <div class="word-list">
        <span>bobcat</span><span>deodorant</span>
        <span>story</span><span>caution</span>
        <span>brush</span><span>lunchroom</span>
        <span>burglar</span><span>sarah</span>
      </div>
    </div>
  </div>

  <div class="phone p3"><span class="sensor"></span><span class="camera"></span>
    <div class="screen">
      <div class="status">
        <svg width="13" height="22"><use href="#ico-back"/></svg>
        <svg width="30" height="30" style="margin-left:10px"><use href="#ico-bolt"/></svg>
        <span class="count">4</span><span class="spacer"></span>
        <svg width="32" height="28"><use href="#ico-heart"/></svg>
        <span class="count">7</span>
      </div>
      <p class="prompt">See the pattern</p>
      <div class="pattern">
        <i class="on"></i><i></i><i></i><i></i><i></i>
        <i></i><i></i><i></i><i></i><i class="on"></i>
        <i></i><i></i><i></i><i></i><i></i>
        <i></i><i></i><i></i><i></i><i class="on"></i>
        <i></i><i></i><i class="on"></i><i class="on"></i><i></i>
      </div>
    </div>
  </div>

  <div class="phone p4"><span class="sensor"></span><span class="camera"></span>
    <div class="screen">
      <div class="status">
        <svg width="13" height="22"><use href="#ico-back"/></svg>
        <svg width="30" height="30" style="margin-left:10px"><use href="#ico-bolt"/></svg>
        <span class="count">0</span><span class="spacer"></span>
        <svg width="32" height="28"><use href="#ico-heart"/></svg>
        <span class="count">0</span>
      </div>
      <p class="prompt">Tap Two Matching Images</p>
      <div class="symbols">
        <span>ध़</span><span>ቋ</span><span>ཙ</span><span>ई</span><span>s</span><span>ረ</span>
        <span>ॅ</span><span>s</span><span>ஃ</span><span>ት</span><span>ध़</span><span>ॅ</span>
        <span>ቋ</span><span>ཙ</span><span>ੲ</span><span>ረ</span><span>ኦ</span><span>ት</span>
        <span>ஃ</span><span>ጉ</span><span>ई</span><span>ਹ</span><span>ਬ</span><span>ኦ</span>
        <span>ጉ</span><span>ਹ</span><span>ஜ</span><span>ਬ</span><span>ፍ</span><span>ॽ</span>
        <span>ॽ</span><span>ᐅ</span><span>ஜ</span><span>ੲ</span><span>ᐅ</span><span>ፍ</span>
      </div>
    </div>
  </div>
</div>
</body>
</html>
```